New professional looking flyer for company

I need our flyer updated my flyer is the Lvb flyer Have attached current flyer so you know what services need to be listed. Want it to be in mainly dark colours like black and dark grey with pops of light grey, silver or white. i have added several photos for you to choose which ones work best with your design would like The photos to be in colour for the flyer. But can have a mix of greyscale if that works for your design j have attached another companies flyers as design ideas to show what I am looking for

Target Market(s)

new clients

Industry/Entity Type

transport and earthmoving

Colors

Designer to choose colors to be used in the design.

Requirements
Nice to have
• Look professional
Should not have
• No orange or red or green

```html
<!DOCTYPE html>
<html lang="en">
<head>
<meta charset="UTF-8">
<title>Lvb Pty Ltd – Services Flyer</title>
<link href="https://fonts.googleapis.com/css2?family=Montserrat:wght@400;500&family=Poppins:wght@600;700;800&display=swap" rel="stylesheet">
<style>
  :root {
    --stage: #363636;
    --black: #000000;
    --ink: #111111;
    --band-grey: #636363;
    --white: #ffffff;
    --silver: #b9b9b9;
    --muted: #8a8a8a;
  }
  * { margin: 0; padding: 0; box-sizing: border-box; }
  html, body { width: 1056px; height: 1200px; overflow: hidden; }
  body { background: var(--stage); position: relative; font-family: "Montserrat", sans-serif; }

  .flyer {
    position: absolute; left: 188px; top: 119px;
    width: 681px; height: 961px;
    background: var(--white); overflow: hidden;
  }
  .hero-photo {
    position: absolute; left: 0; top: 0; width: 681px; height: 267px;
    background: radial-gradient(ellipse at 50% 30%, #3a3a3a 0%, #151515 55%, #070707 100%),
                linear-gradient(180deg, #111 0%, #2b2824 100%);
  }
  .hero-photo::after {
    content: ""; position: absolute; left: 0; right: 0; bottom: 0; height: 70px;
    background: linear-gradient(180deg, rgba(70,64,56,0) 0%, rgba(96,88,78,0.75) 100%);
  }
  .brand {
    position: absolute; left: 0; width: 681px; top: 62px;
    display: flex; justify-content: center; align-items: flex-end; gap: 8px;
    font-family: "Poppins", sans-serif; font-weight: 800; color: var(--silver);
  }
  .brand-name { font-size: 78px; line-height: 1; letter-spacing: 2px; }
  .brand-suffix { font-size: 17px; font-weight: 800; margin-bottom: 8px; color: var(--silver); }

  .headline-box {
    position: absolute; left: 178px; top: 164px; width: 323px; height: 103px;
    background: var(--white);
    display: flex; align-items: center; justify-content: center; text-align: center;
    font-family: "Poppins", sans-serif; font-weight: 700; font-size: 27px; line-height: 0.98;
    color: var(--ink); text-transform: uppercase; letter-spacing: -0.3px;
  }

  .quote-band {
    position: absolute; left: 0; top: 267px; width: 681px; height: 117px;
    background: var(--band-grey);
    display: flex; align-items: center; justify-content: center; text-align: center;
    padding-bottom: 12px;
    font-family: "Poppins", sans-serif; font-weight: 700; font-size: 27px; line-height: 1.02;
    color: var(--white); text-transform: uppercase;
  }
  .services-panel {
    position: absolute; left: 0; top: 384px; width: 681px; height: 427px;
    background: var(--black);
  }
  .divider-bar {
    position: absolute; left: 38px; top: 377px; width: 603px; height: 14px;
    background: var(--white);
  }

  .services-title {
    position: absolute; left: 0; width: 681px; top: 412px; text-align: center;
    font-family: "Poppins", sans-serif; font-weight: 700; font-size: 27px; color: var(--white);
    text-transform: uppercase;
  }
  .service-list { position: absolute; list-style: none; }
  .service-list.left { left: 38px; top: 473px; }
  .service-list.right { left: 393px; top: 473px; }
  .service-item {
    display: flex; align-items: flex-start; gap: 14px;
    color: var(--white); font-size: 17.5px; line-height: 24px;
    margin-bottom: 13px;
  }
  .service-list.right .service-item.two-line { margin-bottom: 14px; }
  .tick { flex: 0 0 23px; width: 23px; height: 23px; margin-top: 0.5px; }

  .site-photo {
    position: absolute; left: 285px; top: 744px; width: 396px; height: 133px;
    clip-path: polygon(0 0, 100% 0, 100% 100%, 79px 100%);
    background: linear-gradient(160deg, #5a5a5a 0%, #7a7a7a 45%, #4a4a4a 100%);
  }
  .contact-tab {
    position: absolute; left: 0; top: 811px; width: 269px; height: 62px;
    background: var(--band-grey);
    clip-path: polygon(0 0, 100% 0, 232px 100%, 0 100%);
  }
  .contact-title {
    position: absolute; left: 38px; top: 826px;
    font-family: "Poppins", sans-serif; font-weight: 700; font-size: 23px; line-height: 32px;
    color: var(--white); text-transform: uppercase;
  }
  .contact-item {
    position: absolute; top: 906px; display: flex; align-items: center; gap: 12px;
    color: var(--ink); font-size: 16px; font-weight: 500;
  }
  .contact-item.phone { left: 38px; }
  .contact-item.email { left: 251px; gap: 10px; }
  .contact-item.address { left: 481px; font-size: 13px; line-height: 12px; gap: 10px; }
  .contact-icon { width: 24px; height: 24px; flex: 0 0 24px; }
</style>
</head>
<body>
  <main class="flyer">
    <div class="hero-photo" role="img" aria-label="Photo of a road train truck at night with a hexagon mesh backdrop"></div>
    <div class="brand"><span class="brand-name">LVB</span><span class="brand-suffix">Pty Ltd</span></div>
    <div class="headline-box">We offer a large<br>range of services<br>not listed</div>

    <div class="quote-band">So call us today for a personalised<br>quote to suit your needs.</div>
    <div class="services-panel"></div>
    <div class="divider-bar"></div>

    <h2 class="services-title">Our Services</h2>

    <ul class="service-list left">
      <li class="service-item"><svg class="tick" viewBox="0 0 24 24"><circle cx="12" cy="12" r="12" fill="#fff"/><path d="M6.5 12.5l3.7 3.7 7.3-7.7" fill="none" stroke="#000" stroke-width="2.8" stroke-linecap="round" stroke-linejoin="round"/></svg>Over size loads / Hot Shot Loads</li>
      <li class="service-item"><svg class="tick" viewBox="0 0 24 24"><circle cx="12" cy="12" r="12" fill="#fff"/><path d="M6.5 12.5l3.7 3.7 7.3-7.7" fill="none" stroke="#000" stroke-width="2.8" stroke-linecap="round" stroke-linejoin="round"/></svg>Heavy Vehicle Recovery Services</li>
      <li class="service-item"><svg class="tick" viewBox="0 0 24 24"><circle cx="12" cy="12" r="12" fill="#fff"/><path d="M6.5 12.5l3.7 3.7 7.3-7.7" fill="none" stroke="#000" stroke-width="2.8" stroke-linecap="round" stroke-linejoin="round"/></svg>Potable Water Deliveries</li>
      <li class="service-item"><svg class="tick" viewBox="0 0 24 24"><circle cx="12" cy="12" r="12" fill="#fff"/><path d="M6.5 12.5l3.7 3.7 7.3-7.7" fill="none" stroke="#000" stroke-width="2.8" stroke-linecap="round" stroke-linejoin="round"/></svg>Road Building / Maintenance</li>
      <li class="service-item"><svg class="tick" viewBox="0 0 24 24"><circle cx="12" cy="12" r="12" fill="#fff"/><path d="M6.5 12.5l3.7 3.7 7.3-7.7" fill="none" stroke="#000" stroke-width="2.8" stroke-linecap="round" stroke-linejoin="round"/></svg>Earthworks</li>
      <li class="service-item"><svg class="tick" viewBox="0 0 24 24"><circle cx="12" cy="12" r="12" fill="#fff"/><path d="M6.5 12.5l3.7 3.7 7.3-7.7" fill="none" stroke="#000" stroke-width="2.8" stroke-linecap="round" stroke-linejoin="round"/></svg>Sand &amp; Metal Supply &amp; Cartage</li>
    </ul>

    <ul class="service-list right">
      <li class="service-item"><svg class="tick" viewBox="0 0 24 24"><circle cx="12" cy="12" r="12" fill="#fff"/><path d="M6.5 12.5l3.7 3.7 7.3-7.7" fill="none" stroke="#000" stroke-width="2.8" stroke-linecap="round" stroke-linejoin="round"/></svg>Road Train Tippers</li>
      <li class="service-item"><svg class="tick" viewBox="0 0 24 24"><circle cx="12" cy="12" r="12" fill="#fff"/><path d="M6.5 12.5l3.7 3.7 7.3-7.7" fill="none" stroke="#000" stroke-width="2.8" stroke-linecap="round" stroke-linejoin="round"/></svg>Road Train Tankers</li>
      <li class="service-item"><svg class="tick" viewBox="0 0 24 24"><circle cx="12" cy="12" r="12" fill="#fff"/><path d="M6.5 12.5l3.7 3.7 7.3-7.7" fill="none" stroke="#000" stroke-width="2.8" stroke-linecap="round" stroke-linejoin="round"/></svg>Road Train Flat Tops</li>
      <li class="service-item"><svg class="tick" viewBox="0 0 24 24"><circle cx="12" cy="12" r="12" fill="#fff"/><path d="M6.5 12.5l3.7 3.7 7.3-7.7" fill="none" stroke="#000" stroke-width="2.8" stroke-linecap="round" stroke-linejoin="round"/></svg>DropDeck Trailers</li>
      <li class="service-item two-line"><svg class="tick" viewBox="0 0 24 24"><circle cx="12" cy="12" r="12" fill="#fff"/><path d="M6.5 12.5l3.7 3.7 7.3-7.7" fill="none" stroke="#000" stroke-width="2.8" stroke-linecap="round" stroke-linejoin="round"/></svg><span>Mine Site Accredited<br>Equipment &amp; Operators</span></li>
      <li class="service-item"><svg class="tick" viewBox="0 0 24 24"><circle cx="12" cy="12" r="12" fill="#fff"/><path d="M6.5 12.5l3.7 3.7 7.3-7.7" fill="none" stroke="#000" stroke-width="2.8" stroke-linecap="round" stroke-linejoin="round"/></svg>Traffic Management</li>
    </ul>

    <div class="site-photo" role="img" aria-label="Aerial greyscale photo of heavy haulage trucks carrying earthmoving machinery"></div>
    <div class="contact-tab"></div>
    <h2 class="contact-title">Contact Us</h2>

    <div class="contact-item phone">
      <svg class="contact-icon" viewBox="0 0 24 24"><circle cx="12" cy="12" r="12" fill="#000"/><path d="M8.2 6.5l2 2.4-1.2 1.5c.8 1.7 2.1 3 3.8 3.8l1.5-1.2 2.4 2-1 1.8c-4.4-.3-8.1-4-8.4-8.4z" fill="#fff"/></svg>
      <span>+00 000 000</span>
    </div>
    <div class="contact-item email">
      <svg class="contact-icon" viewBox="0 0 24 24"><circle cx="12" cy="12" r="12" fill="#000"/><text x="12" y="16.5" text-anchor="middle" font-family="Montserrat, sans-serif" font-size="14" font-weight="500" fill="#fff">@</text></svg>
      <span>info@lvb.com.au</span>
    </div>
    <div class="contact-item address">
      <svg class="contact-icon" viewBox="0 0 24 24"><circle cx="12" cy="12" r="12" fill="#000"/><path d="M12 5.5a4.3 4.3 0 0 0-4.3 4.3c0 3.2 4.3 8 4.3 8s4.3-4.8 4.3-8A4.3 4.3 0 0 0 12 5.5z" fill="#fff"/><circle cx="12" cy="9.8" r="1.6" fill="#000"/></svg>
      <span>123 Anywhere St.,<br>Any City, ST 12345</span>
    </div>
  </main>
</body>
</html>
```